Need Power Point Presentation - That incorporates New Logo

We have a new logo and would like to incorporate it into a Power Point template. We are looking for title page, 2 body pages and a closing page design. If you have any questions please let me know. New logo is attached.

```html
<!DOCTYPE html>
<html lang="en">
<head>
<meta charset="utf-8">
<title>Corvane Presentation Template</title>
<link href="https://fonts.googleapis.com/css2?family=Cinzel:wght@400;600&family=Open+Sans:wght@400;600;700&display=swap" rel="stylesheet">
<style>
:root{
  --stage:#1c1c1c;
  --white:#ffffff;
  --brand:#3f9fd6;
  --brand-deep:#1f7fc0;
  --ink:#2a3a48;
  --navy:#1d4f7a;
  --sky-1:#e6f4fb;
  --sky-2:#b9e0f3;
  --sky-3:#7cc5ea;
  --sky-4:#4fb0e2;
  --band-1:#cdeaf8;
  --band-2:#7fc9ec;
  --muted:#5a6a78;
}
*{box-sizing:border-box;margin:0;padding:0}
html,body{width:1200px;height:712px;overflow:hidden;background:var(--stage)}
.board{display:grid;grid-template-columns:600px 600px;grid-template-rows:356px 356px;width:1200px;height:712px}
.cell{display:flex;align-items:center;justify-content:center}
.slide{position:relative;width:440px;height:330px;background:var(--white);overflow:hidden;box-shadow:0 2px 10px rgba(0,0,0,.5);font-family:"Open Sans",sans-serif;color:var(--ink)}
.wordmark{font-family:"Open Sans",sans-serif;font-weight:600;color:var(--brand);letter-spacing:.06em;display:flex;align-items:center;gap:6px}
.wordmark .dot{width:7px;height:7px;border-radius:50%;background:var(--brand)}
.wordmark.light{color:var(--white)}
.wordmark.light .dot{background:var(--white)}

/* cover */
.cover .wordmark{position:absolute;left:0;right:0;top:140px;justify-content:center;font-size:38px}
.cover .wordmark .dot{width:10px;height:10px}
.cover .url{position:absolute;left:0;right:0;bottom:22px;text-align:center;font-size:8px;color:var(--ink)}

/* title slide */
.title-slide{background:linear-gradient(180deg,var(--sky-1) 0%,var(--sky-2) 55%,var(--sky-1) 100%)}
.title-slide .wordmark{position:absolute;left:22px;top:20px;font-size:17px}
.title-slide .pill{position:absolute;left:0;right:0;top:82px;height:172px;border-radius:0 86px 86px 0;margin-right:-0px;background:linear-gradient(180deg,var(--sky-3) 0%,var(--sky-4) 60%,var(--sky-3) 100%);box-shadow:0 4px 12px rgba(30,100,150,.35)}
.title-slide .pill::before{content:"";position:absolute;left:0;right:50px;top:0;height:56px;border-radius:0 60px 0 0;background:linear-gradient(180deg,rgba(255,255,255,.45),rgba(255,255,255,0))}
.title-slide h1{position:absolute;left:38px;top:152px;font-family:"Cinzel",serif;font-weight:400;font-size:22px;color:var(--white);letter-spacing:.02em}
.title-slide .subtitle{position:absolute;left:40px;top:184px;font-size:8.5px;font-weight:700;color:var(--navy);letter-spacing:.04em}
.title-slide .copyright{position:absolute;left:38px;bottom:34px;font-family:"Cinzel",serif;font-size:7.5px;color:var(--white);letter-spacing:.04em}

/* body slides */
.heading{position:absolute;left:10px;top:16px;display:flex;align-items:center;gap:8px}
.heading .rule{display:flex;flex-direction:column;gap:2px}
.heading .rule span{display:block;width:38px;height:1px;background:var(--sky-3)}
.heading h2{font-family:"Cinzel",serif;font-weight:600;font-size:13px;color:var(--ink);letter-spacing:.03em}
.copy{position:absolute;font-size:7px;line-height:1.45;text-align:justify;color:var(--ink)}
.copy p+p{margin-top:9px}
.photo{position:absolute;left:50px;top:78px;width:128px;height:170px;background:linear-gradient(180deg,#0e2c4c 0%,#2f6b9a 45%,#8ab8d8 70%,#3b4a5a 100%)}
.footer-band{position:absolute;left:10px;right:10px;bottom:10px;height:34px;border-radius:0 17px 17px 0;background:linear-gradient(180deg,var(--band-1),var(--band-2));display:flex;align-items:center;justify-content:space-between;padding:0 16px 0 12px}
.footer-band .num{font-size:7px;color:var(--white);width:20px}
.footer-band .url{font-size:7px;color:var(--white);flex:1}
.footer-band .wordmark{font-size:16px}
.chart{position:absolute;left:232px;top:80px;width:180px;height:150px}
.legend{position:absolute;left:236px;top:238px;display:flex;gap:8px;font-size:5.5px;color:var(--muted)}
.legend i{display:inline-block;width:5px;height:5px;margin-right:2px;vertical-align:middle}
</style>
</head>
<body>
<main class="board">

  <div class="cell">
    <section class="slide cover">
      <div class="wordmark"><span>CORVANE</span><span class="dot"></span></div>
      <p class="url">www.corvane.com</p>
    </section>
  </div>

  <div class="cell">
    <section class="slide content">
      <div class="heading"><div class="rule"><span></span><span></span></div><h2>CONCEPT PLUS PRESENTATION POWERFUL MISSION 1</h2></div>
      <div class="photo" role="img" aria-label="Photograph of a glass office tower lit up at dusk"></div>
      <div class="copy" style="left:222px;top:80px;width:178px">
        <p>The NRF has forged a courageous and dynamic approach to the methodology of cancer research. By overcoming previous pitfalls that held the industry back, the NRF has propelled the frontier of multiple myeloma research to a new level.</p>
        <p>Essential to this approach are 4 revious pitfalls that held the industry back, the NRF has propelled the frontier of multiple myeloma research to a new level. groundbreaking initiatives that have revolutionized the way research and drug development are conducted. With these models, the NRF can dramatically accelerate.</p>
        <p>Groundbreaking initiatives that have revolutionized the way research and drug development are conducted.</p>
      </div>
      <div class="footer-band"><span class="num">5</span><span class="url">www.corvane.com</span><div class="wordmark light"><span>CORVANE</span><span class="dot"></span></div></div>
    </section>
  </div>

  <div class="cell">
    <section class="slide title-slide">
      <div class="wordmark"><span>CORVANE</span><span class="dot"></span></div>
      <div class="pill"></div>
      <h1>PRESENTATION TITTLE HERE</h1>
      <p class="subtitle">YOUR PRESENTATION SUB TITLE HERE</p>
      <p class="copyright">© 2013 Corvane. All rights reserved.</p>
    </section>
  </div>

  <div class="cell">
    <section class="slide content">
      <div class="heading"><div class="rule"><span></span><span></span></div><h2>CONCEPT PLUS PIE CHART SAMPLE HERE</h2></div>
      <div class="copy" style="left:50px;top:80px;width:160px">
        <p>The NRF has forged a courageous and dynamic approach to the methodology of cancer research. By overcoming previous pitfalls that held the industry back, the NRF has propelled the frontier of multiple myeloma research to a new level.</p>
        <p>Essential to this approach revious pitfalls that held the industry back, the NRF has propelled the frontier of multiple myeloma research to a new level. are 4 groundbreaking initiatives that have revolutionized the way research and drug development are conducted. With these models, the NRF can dramatically accelerate the pace at which lifesaving and new life-altering drugs can be brought to patients.</p>
      </div>
      <svg class="chart" viewBox="0 0 180 150" aria-label="Pie chart with four segments">
        <g transform="translate(90,84) scale(1,0.6)">
          <circle r="70" fill="#1a78b4"/>
        </g>
        <g transform="translate(90,72) scale(1,0.6) rotate(-90)">
          <circle r="35" fill="none" stroke="#2aa0dc" stroke-width="70" stroke-dasharray="127.6 220" stroke-dashoffset="0"/>
          <circle r="35" fill="none" stroke="#bfe6f7" stroke-width="70" stroke-dasharray="39.6 220" stroke-dashoffset="-127.6"/>
          <circle r="35" fill="none" stroke="#8ad2f1" stroke-width="70" stroke-dasharray="30.8 220" stroke-dashoffset="-167.2"/>
          <circle r="35" fill="none" stroke="#55b9e8" stroke-width="70" stroke-dasharray="21.9 220" stroke-dashoffset="-198"/>
        </g>
      </svg>
      <div class="legend">
        <span><i style="background:#2aa0dc"></i>Pie Chart 1</span>
        <span><i style="background:#bfe6f7"></i>Pie Chart 2</span>
        <span><i style="background:#8ad2f1"></i>Pie Chart 3</span>
        <span><i style="background:#55b9e8"></i>Pie Chart 4</span>
      </div>
      <div class="footer-band"><span class="num">11</span><span class="url">www.corvane.com</span><div class="wordmark light"><span>CORVANE</span><span class="dot"></span></div></div>
    </section>
  </div>

</main>
</body>
</html>
```